Business Card Design using new logo

As much as we'd like to think that treating everyone equally is the best strategy for fairness, the reality is that the differences in the lives of women and men have to be taken into account to ensure that organizations, programs, services, and yes, even public policy treat women and men in ways that achieve gender equity.

That's where ParityLumen - fairness metrics insight comes in. Using the data-driven tools of gender analysis, our organization can help anyone determine if gender equity is being achieved - in businesses and organizations, in the planning and implementation of programs and services, and in the development and enforcement of public policy.
Updates

Apologies for the delay - have not had time to finalize the decision.  Should be early this week - probably Tuesday.

Industry/Entity Type

Business

Requirements
Must have
• New Logo for ParityLumen
• Logo plus words "Fairness Metrics Insight"

```html
<!DOCTYPE html>
<html lang="en">
<head>
<meta charset="utf-8">
<title>ParityLumen Business Card</title>
<link rel="stylesheet" href="https://fonts.googleapis.com/css2?family=Lato:wght@300;400;700;900&display=swap">
<style>
  :root {
    --stage: #3a4a4c;
    --ink: #0b0b0b;
    --paper: #ffffff;
    --orange: #de8526;
    --orange-light: #f4a13f;
    --text: #1c1c1c;
    --muted: #555555;
    --rule: #222222;
  }
  * { box-sizing: border-box; margin: 0; padding: 0; }
  html, body { width: 1200px; height: 1000px; overflow: hidden; }
  body {
    background: var(--stage);
    font-family: "Lato", sans-serif;
    position: relative;
  }
  .card {
    position: absolute;
    left: 320px;
    width: 560px;
    height: 320px;
    overflow: hidden;
    box-shadow: 0 10px 30px rgba(0,0,0,.35);
  }
  .card--front { top: 150px; background: var(--paper); }
  .card--back { top: 530px; background: var(--ink); }

  /* front: left brand panel */
  .brand-panel {
    position: absolute;
    left: 0; top: 0;
    width: 200px; height: 320px;
  }
  .brand-panel svg { position: absolute; inset: 0; }
  .brand-panel .wordmark {
    position: absolute;
    left: 26px; top: 78px;
    display: flex; align-items: center; gap: 8px;
    color: var(--paper);
    font-size: 22px; font-weight: 400;
  }
  .dot {
    width: 14px; height: 14px; border-radius: 50%;
    background: var(--orange);
    flex: none;
  }

  /* front: details */
  .details {
    position: absolute;
    left: 232px; top: 40px;
    right: 28px;
    color: var(--text);
  }
  .person-name {
    font-size: 24px; font-weight: 300; letter-spacing: .5px;
    line-height: 1;
  }
  .person-name b { font-weight: 900; }
  .person-role {
    font-size: 13px; font-weight: 400; margin-top: 4px;
  }
  .person-role b { font-weight: 700; }
  .company {
    margin-top: 26px;
    font-size: 15px; font-weight: 900; letter-spacing: .6px;
    text-transform: uppercase;
    padding-bottom: 5px;
    border-bottom: 1.5px solid var(--rule);
  }
  .contacts { list-style: none; margin-top: 10px; }
  .contacts li {
    display: flex; align-items: center; gap: 9px;
    font-size: 12px; color: var(--muted);
    line-height: 22px;
  }
  .contacts svg { width: 11px; height: 11px; fill: var(--text); flex: none; }

  /* back */
  .world-map {
    position: absolute;
    left: 70px; top: 40px;
    width: 420px; height: 240px;
    background: radial-gradient(ellipse at center, #1e1e1e 0%, #141414 55%, var(--ink) 80%);
  }
  .card--back .wordmark {
    position: absolute;
    left: 0; right: 0; top: 136px;
    display: flex; justify-content: center; align-items: center; gap: 12px;
    color: var(--paper);
    font-size: 40px; font-weight: 400;
  }
  .card--back .dot { width: 22px; height: 22px; }
</style>
</head>
<body>

<section class="card card--front" aria-label="Business card front">
  <div class="brand-panel">
    <svg width="200" height="320" viewBox="0 0 200 320" aria-hidden="true">
      <rect x="0" y="0" width="200" height="320" fill="var(--ink)"/>
      <polygon points="0,320 0,215 80,190 200,120 200,320" fill="var(--paper)"/>
      <polygon points="6,320 6,222 84,198 200,131 200,320" fill="var(--orange)"/>
    </svg>
    <div class="wordmark"><span class="dot"></span>ParityLumen</div>
  </div>

  <div class="details">
    <h1 class="person-name">MARCUS <b>HALE</b></h1>
    <p class="person-role"><b>Managing</b> Director</p>
    <h2 class="company">Fairness Metrics Insight</h2>
    <ul class="contacts">
      <li>
        <svg viewBox="0 0 24 24" aria-hidden="true"><path d="M6.6 10.8a15 15 0 0 0 6.6 6.6l2.2-2.2a1 1 0 0 1 1-.25 11.4 11.4 0 0 0 3.6.57 1 1 0 0 1 1 1V20a1 1 0 0 1-1 1A17 17 0 0 1 3 4a1 1 0 0 1 1-1h3.5a1 1 0 0 1 1 1c0 1.25.2 2.45.57 3.57a1 1 0 0 1-.25 1z"/></svg>
        + 000 - 4821 - 7306
      </li>
      <li>
        <svg viewBox="0 0 24 24" aria-hidden="true"><path d="M2 5h20v14H2zm2 2v.5l8 5 8-5V7zm0 2.8V17h16V9.8l-8 5z"/></svg>
        admin@paritylumen.com
      </li>
      <li>
        <svg viewBox="0 0 24 24" aria-hidden="true"><path d="M12 2a10 10 0 1 0 0 20 10 10 0 0 0 0-20zm6.9 9h-3a15 15 0 0 0-1.3-6.1A8 8 0 0 1 18.9 11zM12 4.1c.9 1.2 1.8 3.6 1.9 6.9h-3.8c.1-3.3 1-5.7 1.9-6.9zM9.4 4.9A15 15 0 0 0 8.1 11h-3a8 8 0 0 1 4.3-6.1zM5.1 13h3a15 15 0 0 0 1.3 6.1A8 8 0 0 1 5.1 13zm6.9 6.9c-.9-1.2-1.8-3.6-1.9-6.9h3.8c-.1 3.3-1 5.7-1.9 6.9zm2.6-.8a15 15 0 0 0 1.3-6.1h3a8 8 0 0 1-4.3 6.1z"/></svg>
        paritylumen.com
      </li>
      <li>
        <svg viewBox="0 0 24 24" aria-hidden="true"><path d="M12 2a7 7 0 0 0-7 7c0 5.2 7 13 7 13s7-7.8 7-13a7 7 0 0 0-7-7zm0 9.5a2.5 2.5 0 1 1 0-5 2.5 2.5 0 0 1 0 5z"/></svg>
        PO Box 418 Carlton South VIC 3053
      </li>
    </ul>
  </div>
</section>

<section class="card card--back" aria-label="Business card back">
  <div class="world-map" role="img" aria-label="Faint dotted world map in dark grey behind the name"></div>
  <div class="wordmark"><span class="dot"></span>ParityLumen</div>
</section>

</body>
</html>
```